Business Card Tech Company
Veradon Corp
Project: Business Card Tech Company
Business Card Tech Company -
Creative Brief
Simple
Marcel Dufresne
CEO
2745 Rue Belcourt, Québec, QC G2K 3P7, Canada
mdufresne@veradoncorp-example.com
www.veradoncorp-example.com
You can add Twitter @veradoncorp We are very open to different designs, We will provide fast feedback, You can try many styles and many fonts, Right now, our slogan is: the world made yours. You can put it on some designs if it fits well, consider we might want to change it.
We would like a back mostly visual, without much info.

```html
<!DOCTYPE html>
<html lang="en">
<head>
<meta charset="utf-8">
<title>Veradon Corp – Business Card</title>
<link rel="stylesheet" href="https://fonts.googleapis.com/css2?family=Source+Sans+3:wght@400;600;700&display=swap">
<style>
  :root {
    --page-bg: #e9e6e1;
    --card-white: #ffffff;
    --brand-blue: #1a6fb5;
    --brand-blue-deep: #0b4a8c;
    --brand-blue-light: #2c86cc;
    --swoosh-grey: #8a8d91;
    --mark-grey: #6d7075;
    --text-white: #ffffff;
  }
  * { box-sizing: border-box; margin: 0; padding: 0; }
  html, body {
    width: 1200px; height: 780px; overflow: hidden;
    background: var(--page-bg);
    font-family: "Source Sans 3", "Myriad Pro", sans-serif;
  }
  .card {
    position: absolute; left: 100px; top: 104px;
    width: 1000px; height: 572px;
    border-radius: 28px; overflow: hidden;
    background: var(--card-white);
    box-shadow: 0 10px 30px rgba(0,0,0,0.18);
  }
  .card-wave { position: absolute; inset: 0; width: 100%; height: 100%; }
  .brand {
    position: absolute; left: 64px; top: 200px;
    display: flex; align-items: center; gap: 18px;
  }
  .brand-dot {
    width: 74px; height: 74px; border-radius: 50%;
    background: var(--mark-grey);
  }
  .brand-name {
    font-size: 68px; font-weight: 400; color: var(--brand-blue);
    letter-spacing: 0.5px; line-height: 1;
  }
  .person {
    position: absolute; right: 48px; top: 60px;
    text-align: right; color: var(--text-white);
  }
  .person-name { font-size: 30px; font-weight: 700; line-height: 1.1; }
  .person-role { font-size: 18px; font-weight: 400; margin-top: 4px; }
  .contact {
    position: absolute; right: 48px; top: 268px;
    text-align: right; color: var(--text-white);
    font-size: 18px; line-height: 1.3;
  }
  .address { margin-bottom: 24px; }
  .contact-list { list-style: none; }
  .contact-list li {
    display: flex; justify-content: flex-end; align-items: center;
    gap: 10px; height: 28px;
  }
  .icon { width: 18px; height: 18px; flex: none; }
  .icon-square {
    width: 18px; height: 18px; border-radius: 3px;
    background: var(--text-white); flex: none;
  }
</style>
</head>
<body>
  <div class="card">
    <svg class="card-wave" viewBox="0 0 1000 572" preserveAspectRatio="none" aria-hidden="true">
      <defs>
        <linearGradient id="waveBlue" x1="0" y1="0" x2="1" y2="1">
          <stop offset="0" stop-color="#2c86cc"/>
          <stop offset="0.55" stop-color="#1a6fb5"/>
          <stop offset="1" stop-color="#0b4a8c"/>
        </linearGradient>
      </defs>
      <path d="M40 438 C 150 410, 280 400, 380 340 C 300 395, 170 425, 40 438 Z" fill="#8a8d91"/>
      <path d="M600 0 C 575 130, 490 310, 330 395 C 210 458, 80 470, 0 472 L 0 572 L 1000 572 L 1000 0 Z" fill="url(#waveBlue)"/>
    </svg>

    <div class="brand">
      <span class="brand-dot"></span>
      <span class="brand-name">Veradon</span>
    </div>

    <div class="person">
      <p class="person-name">Marcel Dufresne</p>
      <p class="person-role">CEO</p>
    </div>

    <div class="contact">
      <p class="address">2745 Rue Belcourt,<br>Québec, QC, G2K 3P7, Canada</p>
      <ul class="contact-list">
        <li>418-555-0142
          <svg class="icon" viewBox="0 0 18 18"><rect x="5" y="1" width="8" height="16" rx="2" fill="#fff"/><rect x="6.5" y="3" width="5" height="9" fill="#1a6fb5"/></svg>
        </li>
        <li>mdufresne@veradoncorp-example.com
          <svg class="icon" viewBox="0 0 18 18"><rect x="1" y="4" width="16" height="11" rx="2" fill="#fff"/><path d="M2 5 L9 10 L16 5" fill="none" stroke="#1a6fb5" stroke-width="1.5"/></svg>
        </li>
        <li>www.veradoncorp-example.com
          <svg class="icon" viewBox="0 0 18 18"><circle cx="9" cy="9" r="7.5" fill="none" stroke="#fff" stroke-width="1.6"/><ellipse cx="9" cy="9" rx="3" ry="7.5" fill="none" stroke="#fff" stroke-width="1.3"/><line x1="1.5" y1="9" x2="16.5" y2="9" stroke="#fff" stroke-width="1.3"/></svg>
        </li>
        <li>@veradoncorp <span class="icon-square"></span></li>
      </ul>
    </div>
  </div>
</body>
</html>
```